PLUX Safety Poster

We need a safety poster designed that we can provide to our members to put up on the wall of their factories. It needs to be clear and concise and simple but also that they are aware it is provided by us. We would like the poster to be in line with our branding companies, you can view these on our website www.brightvellum.com A3 size please

All files are here https://www.filequay.com/sh/wq7tn2bz5mc8xpe/QRfTzk-LmPaVuWx84Hc3Jb6s?n=47719305

```html
<!DOCTYPE html>
<html lang="en">
<head>
<meta charset="utf-8">
<title>PLUX Safety Poster – Heat Stress Isn't Cool</title>
<link rel="stylesheet" href="https://fonts.googleapis.com/css2?family=Archivo+Black&family=Roboto+Condensed:wght@300;400;700&family=Courier+Prime:wght@400;700&display=swap">
<style>
  :root {
    --page: #e9e9e6;
    --hazard-yellow: #e6b121;
    --hazard-black: #111111;
    --panel-light: #f8da17;
    --panel-mid: #f0b423;
    --panel-edge: #e39a1c;
    --ink: #141414;
    --header-black: #0d0d0d;
    --caution-yellow: #f2c31f;
  }
  * { box-sizing: border-box; margin: 0; padding: 0; }
  html, body {
    width: 1200px; height: 1000px; overflow: hidden;
    background: var(--page);
  }
  .canvas { position: relative; width: 1200px; height: 1000px; }

  .poster {
    position: absolute; left: 50px; top: 100px;
    width: 1100px; height: 800px;
    box-shadow: 0 6px 18px rgba(0,0,0,0.18);
  }
  .poster__stripes { position: absolute; inset: 0; }

  .poster__panel {
    position: absolute; left: 36px; top: 36px; right: 36px; bottom: 36px;
    border-radius: 0 0 22px 22px;
    overflow: hidden;
    background: radial-gradient(ellipse 60% 70% at 72% 42%, var(--panel-light) 0%, var(--panel-mid) 55%, var(--panel-edge) 100%);
  }

  .caution-band {
    position: absolute; left: 0; right: 0; top: 0; height: 110px;
    background: var(--header-black);
    display: flex; align-items: center; justify-content: center;
  }
  .caution-band__title {
    font-family: "Archivo Black", sans-serif;
    font-size: 92px; line-height: 1;
    letter-spacing: 0.36em; margin-right: -0.36em;
    color: var(--caution-yellow);
  }

  .headline { position: absolute; left: 40px; top: 166px; color: var(--ink); }
  .headline__strong {
    display: block;
    font-family: "Archivo Black", sans-serif;
    font-size: 62px; line-height: 1; letter-spacing: -1.5px;
  }
  .headline__light {
    display: block;
    font-family: "Roboto Condensed", sans-serif;
    font-weight: 400;
    font-size: 116px; line-height: 0.95; letter-spacing: -4px;
    margin-top: 2px;
  }

  .advice, .symptoms {
    position: absolute; left: 50px;
    font-family: "Courier Prime", monospace;
    font-weight: 700; font-size: 21px; line-height: 24px;
    color: var(--ink); list-style: none;
    text-transform: uppercase;
  }
  .advice { top: 355px; }
  .symptoms { top: 495px; }
  .symptoms__title { font-family: "Archivo Black", sans-serif; font-weight: 400; font-size: 20px; letter-spacing: 0.2px; }

  .footnote {
    position: absolute; left: 42px; top: 636px; width: 520px;
    font-family: "Courier Prime", monospace;
    font-size: 12.5px; line-height: 15px; color: var(--ink);
    padding-left: 22px; text-indent: -22px;
  }

  .hero-visual {
    position: absolute; left: 680px; top: 150px;
    width: 240px; height: 500px;
    border-radius: 120px 120px 18px 18px;
    background: linear-gradient(180deg, #e2622a 0%, #ef8a2f 18%, #f3e3b3 32%, #e9c98a 55%, #efe0b8 85%, #f5d45c 100%);
  }

  .credit {
    position: absolute; left: 680px; top: 676px;
    font-family: "Roboto Condensed", sans-serif;
    color: var(--ink); line-height: 1;
  }
  .credit__line1 { display: block; font-weight: 700; font-size: 19px; letter-spacing: 0.2px; }
  .credit__line2 { display: block; font-weight: 400; font-size: 21px; margin-top: 1px; }

  .brand-mark {
    position: absolute; left: 860px; top: 678px;
    display: flex; align-items: center; gap: 8px;
    font-family: "Roboto Condensed", sans-serif;
    font-weight: 700; font-size: 13px; line-height: 1.1;
    color: var(--ink); text-transform: uppercase;
  }
  .brand-mark__dot {
    width: 34px; height: 34px; border-radius: 50%;
    background: var(--ink); flex: none;
  }
</style>
</head>
<body>
<main class="canvas">
  <section class="poster">
    <svg class="poster__stripes" width="1100" height="800" viewBox="0 0 1100 800" aria-hidden="true">
      <defs>
        <pattern id="hazard" width="44" height="44" patternUnits="userSpaceOnUse" patternTransform="rotate(-45)">
          <rect width="44" height="44" fill="var(--hazard-yellow)"/>
          <rect width="22" height="44" fill="var(--hazard-black)"/>
        </pattern>
      </defs>
      <rect width="1100" height="800" fill="url(#hazard)"/>
    </svg>

    <div class="poster__panel">
      <header class="caution-band">
        <h1 class="caution-band__title">CAUTION</h1>
      </header>

      <h2 class="headline">
        <span class="headline__strong">HEAT STRESS</span>
        <span class="headline__light">ISN'T COOL</span>
      </h2>

      <ul class="advice">
        <li>Drink plenty of water</li>
        <li>Take breaks</li>
        <li>Wear light clothing when appropriate</li>
        <li>Monitor work mates for signs of heat stress</li>
      </ul>

      <div class="symptoms">
        <p class="symptoms__title">SIGNS OF HEAT STRESS OR HEAT EXHAUSTION</p>
        <p>Feeling sick, weak or clumsy / dizzy.</p>
        <p>Cramps can also be caused by heat</p>
        <p>Discomfort from heat rash</p>
      </div>

      <p class="footnote">** If you have profuse sweating, weakness, nausea or vomiting, headaches and muscle spasms then stop work immediately and seek help.</p>

      <div class="hero-visual" role="img" aria-label="Melting ice cream cone wearing an orange hard hat, dripping onto the ground"></div>

      <p class="credit">
        <span class="credit__line1">THIS IS A PLUX</span>
        <span class="credit__line2">SAFETY POSTER</span>
      </p>

      <div class="brand-mark">
        <span class="brand-mark__dot"></span>
        <span>Guild of Hollow<br>Form Makers</span>
      </div>
    </div>
  </section>
</main>
</body>
</html>
```